KV MERCANTILE HOLDINGS LETTERHEAD

I need letterhead for "KV Mercantile holdings LLC" ...

logo attached to project...

Company Info:
418 North Larkmoor Avenue, Suite 7B
Chicago, Illinois 60417
ofc 312-555-0148
facsimile 312-555-0193
www.kvmercantileholdings.example
info@kvmercantileholdings.example

I have multiple projects listed.. see below:

Business cards for amber ledge partners llc
letterhead
envelopes

Business cards for KV Mercantile LLC
letterhead
envelopes

```html
<!DOCTYPE html>
<html lang="en">
<head>
<meta charset="utf-8">
<title>KV Mercantile Holdings LLC — Letterhead</title>
<link rel="stylesheet" href="https://fonts.googleapis.com/css2?family=Cinzel:wght@400;500&family=Josefin+Sans:wght@400&display=swap">
<style>
  :root {
    --navy: #0d3a6a;
    --navy-text: #1a4677;
    --mist: #c7d5e3;
    --paper: #ffffff;
    --ink-light: #ffffff;
  }
  html, body {
    margin: 0;
    padding: 0;
    width: 924px;
    height: 1200px;
    overflow: hidden;
    background: var(--paper);
  }
  .letterhead {
    position: relative;
    width: 924px;
    height: 1200px;
    overflow: hidden;
    background: var(--paper);
  }
  .brand-mark {
    position: absolute;
    left: 66px;
    top: 158px;
    margin: 0;
    font-family: "Cinzel", serif;
    font-weight: 500;
    font-size: 31px;
    letter-spacing: 0.5px;
    color: var(--navy-text);
    white-space: nowrap;
  }
  .contact-block {
    position: absolute;
    right: 51px;
    top: 28px;
    text-align: right;
  }
  .contact-name {
    margin: 0 0 6px 0;
    padding-right: 18px;
    font-family: "Cinzel", serif;
    font-weight: 500;
    font-size: 17px;
    color: var(--navy-text);
    white-space: nowrap;
  }
  .contact-list {
    list-style: none;
    margin: 0;
    padding: 0;
    font-family: "Josefin Sans", sans-serif;
    font-size: 16.5px;
    color: var(--navy);
  }
  .contact-list li {
    display: flex;
    justify-content: flex-end;
    align-items: center;
    height: 22px;
    white-space: nowrap;
  }
  .contact-list li::after {
    content: "";
    display: inline-block;
    width: 8px;
    height: 8px;
    margin-left: 10px;
    background: var(--navy);
  }
  .backdrop-shape {
    position: absolute;
    left: 500px;
    top: 740px;
    width: 560px;
    height: 560px;
    border-radius: 50%;
    background: var(--mist);
    opacity: 0.85;
  }
  .footer-band {
    position: absolute;
    left: 0;
    bottom: 0;
    width: 924px;
    height: 57px;
    background: var(--navy);
  }
  .footer-name {
    position: absolute;
    right: 30px;
    top: 12px;
    margin: 0;
    font-family: "Cinzel", serif;
    font-weight: 400;
    font-size: 27px;
    color: var(--ink-light);
    white-space: nowrap;
  }
</style>
</head>
<body>
  <main class="letterhead">
    <p class="brand-mark">KV Mercantile Holdings LLC</p>

    <address class="contact-block">
      <p class="contact-name">KV Mercantile Holdings LLC</p>
      <ul class="contact-list">
        <li>418 North Larkmoor Avenue, Suite 7B</li>
        <li>Chicago, Illinois 60417</li>
        <li>ofc 312-555-0148</li>
        <li>facsimile 312-555-0193</li>
        <li>www.kvmercantileholdings.example</li>
        <li>info@kvmercantileholdings.example</li>
      </ul>
    </address>

    <div class="backdrop-shape" aria-hidden="true"></div>

    <footer class="footer-band">
      <p class="footer-name">KV Mercantile Holdings LLC</p>
    </footer>
  </main>
</body>
</html>
```